Velto Business Card

1. We need a double sided business card ready to print by Wed 26 June.
2. Our business name is Velto
3. We trade under the name Velto Consult.
4. The card will be printed by Pib or CardNorra on a 85mmx55mm card with rounded edges (standard size). The card will be on a luxury finish and we dont mind the logo or contact details being embossed in silver or a suitable colour.
5. The card should be simple and classy representing a management consultancy. Slimmer and large fonts should be used
6. Our website is www.veltoconsult.example
7. We dont want a tag line
8. The cards are for three partners, therefore the same design will be used to add details for each of the 3 partners, therefore the files we receive should be editable.
9. The contact details to include as a minimum:
Name First Name Last Name
Position: Partner
Telephone +44 7612 555 123
email: first.last@veltoconsult.example
10. This is our linkedIn Page: https://www.linkedin.example/company/velto-group/ to get an idea of our business (do not use on the card)
11. We want one side to have the logo in the middle, could be silver and embossed with a single dark blue colour in the background.
12. Our accent (>) and contact details should be on the reverse side with a white background, perhaps replace the website with QR code.
13. The text should be legible and large and look classy and professional, maybe slimmer fonts
14. You do not need to keep to the colours we have provided, be creative
15. We want the original files, vectors, jpeg, .ai and .png files ready to print.
16. We want the options to make several revisions to get the card right.

```html
<!DOCTYPE html>
<html lang="en">
<head>
<meta charset="utf-8">
<title>Velto Business Card</title>
<link rel="stylesheet" href="https://fonts.googleapis.com/css2?family=Montserrat:wght@400;700;800&family=Nunito:wght@400;600&display=swap">
<style>
  :root {
    --backdrop: #48507f;
    --navy: #0b1238;
    --navy-soft: #161d47;
    --orange: #f7961d;
    --orange-deep: #f08a12;
    --white: #ffffff;
    --ink: #1a1f3d;
  }
  * { box-sizing: border-box; margin: 0; padding: 0; }
  html, body { width: 1200px; height: 900px; overflow: hidden; }
  body {
    background: var(--backdrop);
    display: flex;
    align-items: center;
    justify-content: center;
    gap: 60px;
  }
  .card {
    position: relative;
    width: 520px;
    height: 336px;
    border-radius: 24px;
    overflow: hidden;
    box-shadow: 0 18px 40px rgba(20, 24, 60, 0.35);
  }
  .card--front { background: var(--white); }
  .card--back {
    background: var(--navy);
    display: flex;
    align-items: center;
    justify-content: center;
  }
  .edge-band { position: absolute; left: 0; bottom: 0; width: 100%; height: 24px; }
  .identity { position: absolute; left: 34px; top: 96px; }
  .identity__name {
    font-family: "Montserrat", sans-serif;
    font-weight: 800;
    font-size: 22px;
    color: var(--orange);
    letter-spacing: 0.2px;
  }
  .identity__role {
    font-family: "Nunito", sans-serif;
    font-size: 12px;
    color: var(--ink);
    margin-top: 2px;
  }
  .identity__rule { width: 46px; height: 2px; background: var(--orange); margin-top: 8px; }
  .contacts { list-style: none; position: absolute; left: 34px; top: 178px; }
  .contacts__item {
    display: flex;
    align-items: center;
    gap: 9px;
    font-family: "Nunito", sans-serif;
    font-size: 13px;
    color: var(--ink);
    letter-spacing: 0.4px;
    line-height: 22px;
    white-space: nowrap;
  }
  .contacts__icon { width: 11px; height: 11px; flex: none; }
  .wordmark {
    font-family: "Montserrat", sans-serif;
    font-weight: 800;
    letter-spacing: -1px;
    line-height: 1;
  }
  .wordmark--front {
    position: absolute;
    right: 44px;
    top: 136px;
    font-size: 50px;
    color: var(--navy);
  }
  .wordmark--back { font-size: 84px; color: var(--navy-soft); }
</style>
</head>
<body>
  <section class="card card--front" aria-label="Business card, contact side">
    <div class="identity">
      <p class="identity__name">Marcus Hale</p>
      <p class="identity__role">Partner</p>
      <div class="identity__rule"></div>
    </div>
    <ul class="contacts">
      <li class="contacts__item">
        <svg class="contacts__icon" viewBox="0 0 12 12"><path d="M2.5 1 L4.5 1 L5.2 3.6 L4 4.6 C4.7 6.2 5.8 7.3 7.4 8 L8.4 6.8 L11 7.5 L11 9.5 C11 10.3 10.3 11 9.5 11 C5 11 1 7 1 2.5 C1 1.7 1.7 1 2.5 1 Z" fill="var(--orange)"/></svg>
        +44 7612 555 123
      </li>
      <li class="contacts__item">
        <svg class="contacts__icon" viewBox="0 0 12 12"><rect x="0.5" y="2" width="11" height="8" rx="1" fill="var(--orange)"/><path d="M1 2.6 L6 6.4 L11 2.6" stroke="#fff" stroke-width="1" fill="none"/></svg>
        first.last@veltoconsult.example
      </li>
      <li class="contacts__item">
        <svg class="contacts__icon" viewBox="0 0 12 12"><circle cx="6" cy="6" r="5" fill="none" stroke="var(--orange)" stroke-width="1.3"/><ellipse cx="6" cy="6" rx="2.2" ry="5" fill="none" stroke="var(--orange)" stroke-width="1"/><line x1="1" y1="6" x2="11" y2="6" stroke="var(--orange)" stroke-width="1"/></svg>
        www.veltoconsult.example
      </li>
    </ul>
    <p class="wordmark wordmark--front">velto</p>
    <svg class="edge-band" viewBox="0 0 520 24" preserveAspectRatio="none" aria-hidden="true">
      <polygon points="0,12 300,12 316,24 0,24" fill="var(--navy)"/>
      <polygon points="300,12 312,4 420,4 430,24 316,24" fill="var(--orange-deep)"/>
    </svg>
  </section>

  <section class="card card--back" aria-label="Business card, logo side">
    <p class="wordmark wordmark--back">velto</p>
  </section>
</body>
</html>
```